Commercial real estate Brokerage logo, letterhead and business card design

Boutique Commercial real Estate Brokerage and development company requires logo, letterhead/stationary and business card design. For reference, competitors include Harper Vale Brightwood, Pemberton & Oakhurst, Renwick Galloway and Tamsin which all have designs which evoke strong corporate image.
Updates

The name of the firm is Brantley Real Estate. If you look at my competitors web sites you will see their logos. I am looking for something that has a similar flavor - not the same colors or graphics - just how you feel when you see their logo. 
1. www.hvb-realty.example
2. http://www.tamsinprop.example/en-us
3. http://www.pembertonoakhurst.example/

Industry/Entity Type

Real Estate

```html
<!DOCTYPE html>
<html lang="en">
<head>
<meta charset="utf-8">
<title>Brantley Real Estate – Stationery</title>
<link href="https://fonts.googleapis.com/css2?family=Open+Sans:wght@400;600;700&display=swap" rel="stylesheet">
<style>
  :root {
    --brand-red: #b5102a;
    --ink: #2b2b2b;
    --muted: #6a6a6a;
    --paper: #ffffff;
    --backdrop: #c8d0d0;
  }
  * { box-sizing: border-box; margin: 0; padding: 0; }
  html, body { width: 1200px; height: 1000px; overflow: hidden; }
  body {
    background: var(--backdrop);
    font-family: "Open Sans", Arial, sans-serif;
    color: var(--ink);
    position: relative;
  }
  .sheet {
    position: absolute;
    background: var(--paper);
    box-shadow: 0 2px 6px rgba(0,0,0,.12);
    overflow: hidden;
  }
  .corner-accent { position: absolute; right: 0; bottom: 0; display: block; }

  /* Wordmark */
  .wordmark { display: flex; align-items: center; gap: 10px; }
  .wordmark-square { width: 26px; height: 26px; background: var(--brand-red); }
  .wordmark-name { font-weight: 700; color: var(--ink); letter-spacing: 1px; line-height: 1; }
  .wordmark-sub { font-weight: 700; color: var(--ink); letter-spacing: 3px; font-size: 7px; margin-top: 3px; }

  /* Letterhead */
  .letterhead { left: 580px; top: 100px; width: 560px; height: 792px; }
  .letterhead .wordmark { position: absolute; left: 52px; top: 78px; }
  .letterhead .wordmark-name { font-size: 22px; }
  .sender-address {
    position: absolute; right: 60px; top: 52px;
    font-size: 9px; line-height: 1.45; color: var(--muted); text-align: left;
  }
  .letter-date { position: absolute; right: 60px; top: 140px; font-size: 9px; color: var(--muted); }
  .letter-body {
    position: absolute; left: 52px; right: 60px; top: 220px;
    font-size: 11px; line-height: 1.7; color: var(--ink);
  }
  .letter-body p { margin-bottom: 22px; }
  .signoff-role { margin-top: 28px; }
  .signoff-name { margin-top: 22px; }

  /* Business cards */
  .card { width: 380px; height: 220px; }
  .card-front { left: 90px; top: 190px; display: flex; align-items: center; justify-content: center; }
  .card-front .wordmark-square { width: 58px; height: 58px; }
  .card-front .wordmark-name { font-size: 40px; color: var(--brand-red); }
  .card-back { left: 90px; top: 480px; }
  .card-back .wordmark { position: absolute; left: 28px; top: 40px; }
  .card-back .wordmark-name { font-size: 16px; }
  .card-back .wordmark-square { width: 20px; height: 20px; }
  .card-details { position: absolute; left: 190px; top: 38px; font-size: 10px; line-height: 1.5; }
  .holder-name { font-weight: 700; font-size: 11px; }
  .holder-role { font-weight: 600; color: var(--brand-red); margin-bottom: 8px; }
  .firm-name { font-weight: 700; }
  .card-contact { margin-top: 8px; }
</style>
</head>
<body>

  <section class="sheet letterhead">
    <div class="wordmark">
      <span class="wordmark-square"></span>
      <div>
        <div class="wordmark-name">BRANTLEY</div>
        <div class="wordmark-sub">REAL ESTATE</div>
      </div>
    </div>
    <address class="sender-address" style="font-style:normal">
      Northgate Offices<br>
      48 Alder Street, 12th Floor<br>
      Northfield, NY 10999<br>
      www.brantley-re.example<br>
      info@brantley-re.example
    </address>
    <div class="letter-date">February 27 , 2014</div>
    <div class="letter-body">
      <p>Mr Owen Marsh</p>
      <p>Lorem ipsum dolor sit amet, consectetuer adipiscing elit, sed diam nonummy nibh euismod tincidunt ut laoreet dolore magna aliquam erat volutpat. Ut wisi enim ad minim veniam, quis nostrud exerci tation ullamcorper suscipit lobortis nisl ut aliquip ex ea commodo consequat. Duis autem vel eum iriure dolor in hendrerit in vulputate velit esse molestie consequat, vel illum dolore eu feugiat nulla facilisis at vero eros et accumsan et iusto odio dignissim qui blandit praesent luptatum zzril delenit augue duis dolore te feugait nulla facilisi.</p>
      <p>Sed ut perspiciatis,<br>unde omnis iste natus error sit voluptatem accusantium doloremque laudantium, totam rem aperiam eaque ipsa, quae ab illo inventore veritatis et quasi architecto beatae vitae dicta sunt, explicabo. nemo enim ipsam voluptatem, quia voluptas</p>
      <div class="signoff-role">Assistant Manager</div>
      <div class="signoff-name">Liam Carver</div>
    </div>
    <svg class="corner-accent" width="70" height="130" viewBox="0 0 70 130" aria-hidden="true">
      <polygon points="70,0 70,130 0,130" fill="var(--brand-red)"/>
    </svg>
  </section>

  <section class="sheet card card-front">
    <div class="wordmark">
      <span class="wordmark-square"></span>
      <span class="wordmark-name">BRANTLEY</span>
    </div>
  </section>

  <section class="sheet card card-back">
    <div class="wordmark">
      <span class="wordmark-square"></span>
      <div>
        <div class="wordmark-name">BRANTLEY</div>
        <div class="wordmark-sub">REAL ESTATE</div>
      </div>
    </div>
    <div class="card-details">
      <div class="holder-name">Mr. OWEN MARSH</div>
      <div class="holder-role">Assistant Manager</div>
      <div class="firm-name">Brantley Real Estate</div>
      <div>48 Alder Street, 12th Floor<br>Northfield, NY 10999</div>
      <div class="card-contact">T: +1 555 013 4821<br>F: +1 555 013 4822</div>
    </div>
    <svg class="corner-accent" width="80" height="26" viewBox="0 0 80 26" aria-hidden="true">
      <polygon points="80,0 80,26 0,26" fill="var(--brand-red)"/>
    </svg>
  </section>

</body>
</html>
```